Need posters that inspire entrepreneurs

I want to create beautiful, inspiring wall art. I'm looking for a designer to create an awesome sample (note this sample is not for real use). The winning design will form the foundation of our art "style" so there will be LOTS of ongoing work for the winning designer.

It's your challenge to create a style that is clean, inspiring and timeless, and possibly can be adapted to different colour palettes.

Looking for a perfect execution of words, image and design.

The attached example shows one idea. It should serve as an idea only.

Format of the images should be either rectangular or square. Exact size is preferably UK A4 (US letter) or max A3. Assume that a display would consist of a 4 x 4 image grid so size needs to allow for that in a small to medium size office.

The quotes I want in the 3 samples (each in an individual poster - not combined in 1 poster). Each quote should have it's own, the reason for three is to prove the design work on more than one quote. The quotes are:

1) Failure is the condiment that gives success its flavor.
– Dorian Welsby

2) Whether you think you can or think you can’t, you’re right.
– Oswald Pike

3) Ever tried. Ever failed. No matter. Try Again. Fail again. Fail better.
– Lionel Marwick

Each design should include the image of the person and the quote + any design elements you consider relevant. You should find relevant images of the individuals being quoted. The final images will not be published or used commercially in any way.

Font styles to use
Serif
Sans Serif

Colors

Designer to choose colors to be used in the design.

Requirements
Must have
• Words and headshot image - 1 per poster design.
• Please consider in the design that there will not always be photographs of the person quoted and as such the design will need to hold, whether the source is a photo, sketch or something else.
Nice to have
• None, but note that the final image will be printed on a wall mounted board, printed to the edge but not on the edge. The board will have black or white edges so consider in the design.
Should not have
• None

```html
<!DOCTYPE html>
<html lang="en">
<head>
<meta charset="utf-8">
<title>Quote Poster Series</title>
<link rel="stylesheet" href="https://fonts.googleapis.com/css2?family=League+Gothic&family=Open+Sans:wght@700&display=swap">
<style>
  :root {
    --board: #2b2b2d;
    --peach: #f4c3a8;
    --teal: #4b9ba6;
    --yellow: #f6c32b;
    --ink: #0c0d0f;
    --paper: #f3f3f3;
    --label: #f6c32b;
  }
  * { margin: 0; padding: 0; box-sizing: border-box; }
  html, body { width: 1200px; height: 1200px; overflow: hidden; }
  body { background: var(--board); position: relative; font-family: "League Gothic", "Arial Narrow", sans-serif; }

  .poster { position: absolute; border: 10px solid var(--frame); background: var(--ink); overflow: hidden; }
  .poster--peach { --frame: var(--peach); }
  .poster--teal { --frame: var(--teal); }
  .poster--yellow { --frame: var(--yellow); }
  .poster--portrait { width: 342px; height: 440px; }
  .poster--landscape { width: 440px; height: 340px; }

  .poster__photo { position: absolute; inset: 0; }

  .poster__quote {
    position: absolute;
    color: var(--paper);
    text-transform: uppercase;
    font-size: var(--fs, 44px);
    line-height: var(--lh, 38px);
    letter-spacing: 0.2px;
    white-space: nowrap;
  }
  .poster__quote span { display: block; }
  .poster__quote--center { text-align: center; transform: translateX(-50%); }

  .poster__author {
    position: absolute;
    color: var(--paper);
    text-transform: uppercase;
    font-size: 17px;
    letter-spacing: 0.3px;
    white-space: nowrap;
    transform: translateX(-50%);
  }

  .series-label {
    position: absolute;
    left: 212px; top: 900px;
    transform: translateX(-50%);
    text-align: center;
    font-family: "Open Sans", Arial, sans-serif;
    font-weight: 700;
    font-size: 44px;
    line-height: 56px;
    color: var(--label);
  }
</style>
</head>
<body>

  <!-- Lionel Marwick, portrait -->
  <section class="poster poster--portrait poster--peach" style="left:70px;top:24px">
    <div class="poster__photo" role="img" aria-label="Portrait photograph of Lionel Marwick, grey-haired man in a dark jumper"
         style="background:radial-gradient(ellipse 55% 45% at 68% 28%, #7d726c 0%, #3c3634 55%, #141416 100%)"></div>
    <p class="poster__quote poster__quote--center" style="left:86px;top:160px">
      <span>Ever tried.</span><span>Ever failed.</span><span>No matter.</span><span>Try again.</span><span>Fail again.</span><span>Fail better.</span>
    </p>
    <p class="poster__author" style="left:86px;top:396px">Lionel Marwick</p>
  </section>

  <!-- Dorian Welsby, portrait -->
  <section class="poster poster--portrait poster--teal" style="left:430px;top:24px">
    <div class="poster__photo" role="img" aria-label="Monochrome photograph of Dorian Welsby wearing glasses, suit and tie"
         style="background:radial-gradient(ellipse 50% 50% at 78% 45%, #6d8e96 0%, #2f4248 55%, #0d1113 100%)"></div>
    <p class="poster__quote" style="left:16px;top:82px;--lh:43px;--fs:48px">
      <span>Failure</span><span>is the</span><span>condiment</span><span>that gives</span><span>success</span><span>its flavor.</span>
    </p>
    <p class="poster__author" style="left:120px;top:370px">Dorian Welsby</p>
  </section>

  <!-- Oswald Pike, portrait -->
  <section class="poster poster--portrait poster--yellow" style="left:788px;top:24px">
    <div class="poster__photo" role="img" aria-label="Photograph of Oswald Pike standing in a long coat and bowler hat"
         style="background:linear-gradient(90deg, #0e1416 0%, #1f3036 45%, #3b4f55 75%, #1a2428 100%)"></div>
    <p class="poster__quote poster__quote--center" style="left:92px;top:54px">
      <span>Whether</span><span>you think</span><span>you can</span><span>or think</span><span>you can’t,</span><span>you’re</span><span>right.</span>
    </p>
    <p class="poster__author" style="left:92px;top:352px">Oswald Pike</p>
  </section>

  <!-- Dorian Welsby, landscape -->
  <section class="poster poster--landscape poster--teal" style="left:128px;top:480px">
    <div class="poster__photo" role="img" aria-label="Black and white photograph of Dorian Welsby holding a cat"
         style="background:linear-gradient(90deg, #141516 0%, #2a2b2c 35%, #8a8a8a 70%, #4a4a4a 100%)"></div>
    <p class="poster__quote" style="left:16px;top:16px;--lh:42px;--fs:48px">
      <span>Failure</span><span>is the</span><span>condiment</span><span>that gives</span><span>success</span><span>its flavor.</span>
    </p>
    <p class="poster__author" style="left:58px;top:296px">Dorian Welsby</p>
  </section>

  <!-- Lionel Marwick, landscape -->
  <section class="poster poster--landscape poster--peach" style="left:632px;top:480px">
    <div class="poster__photo" role="img" aria-label="Photograph of Lionel Marwick seated in a dark suit wearing glasses"
         style="background:linear-gradient(90deg, #1e3a44 0%, #2c5664 40%, #1a3540 70%, #0a1418 100%)"></div>
    <p class="poster__quote poster__quote--center" style="left:303px;top:22px;--lh:42px;--fs:48px">
      <span>Ever tried.</span><span>Ever failed.</span><span>No matter.</span><span>Try again.</span><span>Fail again.</span><span>Fail better.</span>
    </p>
    <p class="poster__author" style="left:303px;top:282px">Lionel Marwick</p>
  </section>

  <!-- Oswald Pike, landscape -->
  <section class="poster poster--landscape poster--yellow" style="left:380px;top:836px">
    <div class="poster__photo" role="img" aria-label="Photograph of Oswald Pike in profile, chin resting on his hand"
         style="background:radial-gradient(ellipse 45% 60% at 68% 45%, #5a7178 0%, #243238 55%, #0b0f11 100%)"></div>
    <p class="poster__quote poster__quote--center" style="left:90px;top:14px">
      <span>Whether</span><span>you think</span><span>you can</span><span>or think</span><span>you can’t,</span><span>you’re</span><span>right.</span>
    </p>
    <p class="poster__author" style="left:90px;top:292px">Oswald Pike</p>
  </section>

  <p class="series-label">Two<br>orientation<br>of each<br>poster</p>

</body>
</html>
```